Infographics for Zenfolk

Zenfolk company specializes in providing services for the organization of low-budget crowdsourcing research.
Crowdsourcing research - the solution of the problem by lots of people on a competitive basis. Types of research will not be limited to the design competition, and will cover all areas of economic activity.

The site contains the following sections: directory of research, user communities, where they can organize the communication according to common interests, forum, news ticker.

The site will feature two groups of users:
1. Organizers of commercial research - the firm or individual businessmen
2. Researchers of commercial research. Moreover, the organizers can act as executors in the research organized by other users.

Motives Organizers of research:
1. Solving business problems quickly and inexpensively, and the variability of solutions.
2. The possibility of recruiting the best researchers.
3. Self-promotion (positioning your company as an innovative, using cutting-edge technology solutions).
4. Doing Business with the times.

The motives of researchers:
1. Earnings with their knowledge by participating in competitions and receive the prize fund.
2. Employability organized research (if the customer makes an offer the researcher).
3. Intelligent Leisure
4. Communication: forum, chat with the professionals of their field of study.

Required:
Graphically show the behavior of two groups of people based on their motives.
Schematically, the sheet should be divided into two parts - the left diagram of the model of the organizers, to the right - the researchers. The middle - it is desirable that part where the researchers will provide solutions to problems of the organizers - the scheme intersect each other graphically.
This work will be used for placement on the website of the company, as well as in printed promotional products.

Target Market(s)

Entrepreneurs, businesses as well as economically active population of Russia

Industry/Entity Type

Communication

Requirements
Must have
• The company's logo from the attached file.
All decals made with cursive. All decails are editable.
The source file in vector format EPS.
Nice to have
• The color scheme of the site will match the logo, so it is desirable that the figure used the same color as the logo: black, gray, green. In an attachment, "firm color" color settings in the CMYK.
Schemes must come from the top down, page orientation - portrait.
Should not have
• Do not use photos. Only pictures.

```html
<!DOCTYPE html>
<html lang="en">
<head>
<meta charset="utf-8">
<title>Zenfolk — Motives of Organizers and Researchers</title>
<link href="https://fonts.googleapis.com/css2?family=Archivo+Black&display=swap" rel="stylesheet">
<style>
  :root {
    --yellow: #ffd200;
    --yellow-deep: #f6c300;
    --gray-dark: #3c3d3f;
    --gray-mid: #5d5e61;
    --gray-light: #8a8b8e;
    --green: #5cb848;
    --green-light: #79cc5e;
    --green-deep: #3f9a36;
    --ink: #2f3032;
    --white: #ffffff;
    --silver: #d9dadc;
    --silver-dark: #a7a9ac;
  }
  * { box-sizing: border-box; margin: 0; padding: 0; }
  html, body { width: 800px; height: 1200px; overflow: hidden; }
  body {
    position: relative;
    background: radial-gradient(ellipse at 50% 40%, var(--yellow) 0%, var(--yellow-deep) 100%);
    font-family: "Archivo Black", "Arial Black", sans-serif;
    text-transform: uppercase;
  }
  .group-title {
    position: absolute;
    top: 58px;
    width: 350px;
    height: 97px;
    border-radius: 12px;
    padding: 6px;
    background: linear-gradient(#f2f2f3, var(--silver-dark));
    box-shadow: 0 3px 6px rgba(0,0,0,.25);
  }
  .group-title span {
    display: flex;
    align-items: center;
    justify-content: center;
    height: 100%;
    border-radius: 8px;
    color: var(--white);
    font-size: 35px;
    letter-spacing: -0.5px;
  }
  .group-title--organizers { left: 45px; }
  .group-title--organizers span { background: linear-gradient(var(--gray-mid), var(--gray-dark)); }
  .group-title--researchers { left: 403px; }
  .group-title--researchers span { background: linear-gradient(var(--green-light), var(--green)); }

  .motive-row { position: absolute; left: 45px; width: 708px; height: 156px; }
  .motive-row--1 { top: 209px; }
  .motive-row--2 { top: 407px; }
  .motive-row--3 { top: 604px; }
  .motive-row--4 { top: 802px; }

  .pill {
    position: absolute;
    top: 0;
    height: 156px;
    border-radius: 78px;
    box-shadow: 0 3px 8px rgba(0,0,0,.3);
  }
  .pill--organizer {
    left: 0;
    width: 420px;
    background: linear-gradient(var(--gray-mid), var(--gray-dark) 55%, var(--gray-light));
  }
  .pill--researcher {
    left: 313px;
    width: 395px;
    background: linear-gradient(var(--green-light), var(--green) 60%, var(--green-deep));
    box-shadow: -4px 2px 10px rgba(0,0,0,.35);
  }
  .icon-ring {
    position: absolute;
    top: 0;
    width: 156px;
    height: 156px;
    border-radius: 50%;
    padding: 7px;
    background: linear-gradient(#f6f6f7, var(--silver-dark));
    box-shadow: 0 2px 6px rgba(0,0,0,.3);
  }
  .icon-ring--left { left: 0; }
  .icon-ring--right { right: 0; }
  .icon-area { width: 100%; height: 100%; border-radius: 50%; }
  .icon-ring--left .icon-area { background: radial-gradient(circle, #6a6b6e, var(--gray-dark)); }
  .icon-ring--right .icon-area { background: radial-gradient(circle, var(--green-light), var(--green)); }

  .motive-text {
    position: absolute;
    top: 0;
    height: 156px;
    display: flex;
    flex-direction: column;
    justify-content: center;
    font-size: 21px;
    line-height: 23px;
    letter-spacing: -0.6px;
  }
  .motive-text--organizer { left: 164px; color: var(--white); }
  .motive-text--researcher { right: 163px; text-align: right; color: var(--white); }
  .accent-green { color: var(--green-light); }
  .accent-ink { color: var(--ink); }

  .brand-band {
    position: absolute;
    left: 0;
    top: 1021px;
    width: 800px;
    height: 118px;
    background: var(--white);
    display: flex;
    align-items: center;
    justify-content: center;
    gap: 14px;
  }
  .brand-dot { width: 40px; height: 40px; border-radius: 50%; background: var(--green); }
  .brand-name { font-size: 48px; color: var(--gray-dark); text-transform: none; letter-spacing: 0; }
</style>
</head>
<body>
  <div class="group-title group-title--organizers"><span>Organizers</span></div>
  <div class="group-title group-title--researchers"><span>Researchers</span></div>

  <section class="motive-row motive-row--1">
    <div class="pill pill--organizer"></div>
    <div class="pill pill--researcher"></div>
    <div class="icon-ring icon-ring--left"><div class="icon-area" role="img" aria-label="Light bulb with a dollar sign"></div></div>
    <div class="icon-ring icon-ring--right"><div class="icon-area" role="img" aria-label="Number one award rosette"></div></div>
    <p class="motive-text motive-text--organizer"><span>Solve</span><span>Business</span><span class="accent-green">Problems</span></p>
    <p class="motive-text motive-text--researcher"><span class="accent-ink">Received</span><span><span class="accent-ink">The </span>Prize <span class="accent-ink">Fund</span></span><span><span class="accent-ink">In </span>Competitions</span></p>
  </section>

  <section class="motive-row motive-row--2">
    <div class="pill pill--organizer"></div>
    <div class="pill pill--researcher"></div>
    <div class="icon-ring icon-ring--left"><div class="icon-area" role="img" aria-label="Group of people with one highlighted"></div></div>
    <div class="icon-ring icon-ring--right"><div class="icon-area" role="img" aria-label="Handshake"></div></div>
    <p class="motive-text motive-text--organizer"><span class="accent-green">Recruit</span><span>The <span class="accent-green">Best</span></span></p>
    <p class="motive-text motive-text--researcher"><span><span class="accent-ink">Employ</span>ment</span></p>
  </section>

  <section class="motive-row motive-row--3">
    <div class="pill pill--organizer"></div>
    <div class="pill pill--researcher"></div>
    <div class="icon-ring icon-ring--left"><div class="icon-area" role="img" aria-label="Web page with chart and computer mouse"></div></div>
    <div class="icon-ring icon-ring--right"><div class="icon-area" role="img" aria-label="People talking in pairs"></div></div>
    <p class="motive-text motive-text--organizer"><span class="accent-green">Self</span><span>Promotion</span></p>
    <p class="motive-text motive-text--researcher"><span>Intelligent</span><span class="accent-ink">Leisure</span></p>
  </section>

  <section class="motive-row motive-row--4">
    <div class="pill pill--organizer"></div>
    <div class="pill pill--researcher"></div>
    <div class="icon-ring icon-ring--left"><div class="icon-area" role="img" aria-label="Stack of banknotes"></div></div>
    <div class="icon-ring icon-ring--right"><div class="icon-area" role="img" aria-label="Two connected computers with chat bubbles"></div></div>
    <p class="motive-text motive-text--organizer"><span class="accent-green">Do</span><span>Business</span></p>
    <p class="motive-text motive-text--researcher"><span><span class="accent-ink">Communi</span>cation</span></p>
  </section>

  <footer class="brand-band">
    <span class="brand-dot"></span>
    <span class="brand-name">Zenfolk</span>
  </footer>
</body>
</html>
```